DL Cards to get buyers attention

I’m looking to have four double-sided DL flyers professionally prepared and made print-ready in high resolution.

I have uploaded the four existing designs, and I’m happy for them to be reviewed with a fresh set of eyes. While I’m generally happy with the direction, I’m very open to recommendations around layout, typography, imagery, colour balance, spacing and overall presentation if there are opportunities to create a stronger and more professional result.

The key objective is to develop a consistent and recognisable suite of marketing material that strengthens both Fen Calder brand awareness and my personal profile in the local real estate market. Each flyer should feel like part of the same campaign while still having its own clear message and purpose.

I want the finished designs to feel professional, confident, modern and premium, without becoming overly busy or losing the simplicity that makes a DL flyer easy to read. Strong headlines, clear messaging and an obvious call to action are important. The Fen Calder branding should be immediately recognisable, while my photograph, name and contact details should be incorporated naturally and consistently.

Please review the existing designs and suggest any changes that would improve their visual impact, readability and consistency. I’m also open to seeing an alternative design direction if you believe there is a better overall look.

The final artwork needs to be supplied professionally print-ready at DL size (210 mm × 99 mm), double-sided, high resolution, CMYK where appropriate, with 3 mm bleed and safe margins, so it can be provided directly to a commercial printer.

The overall goal is simple: strong branding, professional presentation, consistent recognition and marketing material that people will remember.

Target Market(s)

People looking at selling their homes

Industry/Entity Type

Real Estate

Font styles to use
Serif
Sans Serif

Requirements
Must have
• Strong brand awareness - Fen Calder
Nice to have
• bright and fresh

```html
<!DOCTYPE html>
<html lang="en">
<head>
<meta charset="utf-8">
<title>Fen Calder – DL Flyer Suite</title>
<link href="https://fonts.googleapis.com/css2?family=Montserrat:wght@400;500;600;700;800;900&family=Oswald:wght@500;700&family=Great+Vibes&display=swap" rel="stylesheet">
<style>
:root{
  --yellow:#ffe600;
  --yellow-soft:#fff6b8;
  --pale:#fffbe0;
  --ink:#1b1b1b;
  --body:#4a4a4a;
  --board:#97989b;
  --white:#ffffff;
  --sans:'Montserrat',sans-serif;
  --cond:'Oswald',sans-serif;
  --script:'Great Vibes',cursive;
}
*{box-sizing:border-box;margin:0;padding:0}
html,body{width:1200px;height:1200px;overflow:hidden}
body{background:var(--board);font-family:var(--sans);color:var(--ink);position:relative}
.card{position:absolute;width:498px;height:235px;overflow:hidden;background:var(--white);box-shadow:0 3px 8px rgba(0,0,0,.35)}
.abs{position:absolute}
.col-l{left:98px}.col-r{left:603px}
.row-1{top:66px}.row-2{top:347px}.row-3{top:628px}.row-4{top:909px}
.photo{position:absolute;inset:0}
.brand-tile{position:absolute;top:0;left:436px;width:52px;height:52px;background:var(--yellow);display:flex;align-items:flex-end;justify-content:center;padding-bottom:7px;font:700 7px/1 var(--sans);color:var(--ink)}
.script{font-family:var(--script);font-weight:400}
.icon{width:10px;height:10px;fill:none;stroke:var(--ink);stroke-width:1.6;stroke-linecap:round;stroke-linejoin:round}
.icon-box{display:inline-flex;align-items:center;justify-content:center;background:var(--yellow);flex:none}

/* Steps of a sale – front */
.steps-photo{background:linear-gradient(180deg,#2e4763 0%,#6d87a0 30%,#8aa0a8 40%,#1fa0a6 52%,#3cc0bd 62%,#d4cbb6 78%,#e8dcc6 100%)}
.steps-title{left:17px;top:8px;font:900 42px/0.95 var(--sans);color:var(--white);letter-spacing:-1px}
.steps-title span{color:var(--yellow)}
.steps-sub{left:17px;top:102px;width:150px;font:500 7.5px/1.35 var(--sans);color:var(--white)}
.site-url{right:8px;bottom:6px;font:600 6.5px/1 var(--sans);color:var(--white)}

/* Steps of a sale – back */
.step-col{top:6px;width:97px;height:222px}
.step-head{display:flex;align-items:center;gap:3px;height:24px}
.step-num{width:15px;height:20px;background:var(--yellow);font:800 15px/20px var(--sans);text-align:center;color:var(--ink)}
.step-title{font:600 7px/1.05 var(--sans);text-transform:uppercase}
.step-item{display:flex;gap:3px;margin-top:5px}
.step-item .icon-box{width:11px;height:11px}
.step-item .icon{width:8px;height:8px}
.step-item h4{font:700 5.6px/1.2 var(--sans)}
.step-item p{font:400 4.9px/1.3 var(--sans);color:var(--body)}
.tip{position:absolute;left:0;right:2px;bottom:0;height:38px;background:var(--pale);padding:3px 4px;font:400 4.6px/1.3 var(--sans);color:var(--body)}
.tip b{display:block;font:700 5px/1.2 var(--sans);color:var(--ink)}
.agent-panel{left:415px;top:0;width:83px;height:235px;background:linear-gradient(180deg,#f4f1e8 0%,#e9e3d2 45%,#d9cdb0 100%)}
.agent-note{left:6px;top:54px;width:75px;font:400 5.3px/1.3 var(--sans)}
.agent-call{left:6px;top:86px;font:400 4.8px/1 var(--sans)}
.agent-call span{display:block;font:italic 500 8px/1.2 var(--sans);margin-top:1px}
.agent-photo{left:6px;top:108px;width:72px;height:100px;background:linear-gradient(180deg,#d8d2c2,#f6f6f4)}
.agent-name{left:7px;top:190px;font-size:15px}
.phone-bar{left:0;bottom:0;width:83px;height:18px;background:var(--yellow);display:flex;align-items:center;justify-content:center;gap:3px;font:700 8px/1 var(--sans)}
.phone-dot{width:8px;height:8px;border-radius:50%;background:var(--ink);display:inline-flex;align-items:center;justify-content:center}
.phone-dot svg{width:5px;height:5px;fill:var(--yellow)}

/* Ten things – front */
.sunset-photo{background:linear-gradient(180deg,#1f3044 0%,#3a4e68 30%,#b58b4a 48%,#f6c442 55%,#3b3a3c 62%,#5b6f86 78%,#23344a 100%)}
.ten-title{left:17px;top:6px;font:800 22.5px/1.02 var(--sans);color:var(--white);white-space:nowrap}
.ten-title span{color:var(--yellow);display:block}
.ten-script{left:16px;top:78px;font-size:28px;color:var(--white);transform:rotate(-5deg)}
.ten-rule{left:196px;top:36px;width:2px;height:40px;background:var(--yellow)}
.ten-note{left:210px;top:32px;width:95px;font:500 7.5px/1.33 var(--sans);color:var(--white)}

/* Ten things – back */
.tip-grid{left:7px;top:7px;width:355px;display:grid;grid-template-columns:repeat(5,67px);grid-auto-rows:84px;gap:5px}
.tip-card{position:relative;border:1px solid #efe39a;background:linear-gradient(180deg,var(--white) 0%,var(--pale) 100%);padding:4px}
.tip-card .n{position:absolute;top:2px;right:2px;width:13px;height:12px;background:var(--yellow);font:800 9px/12px var(--sans);text-align:center}
.tip-card .icon{width:11px;height:11px}
.tip-card h4{margin-top:2px;font:700 5.4px/1.15 var(--sans);text-transform:uppercase;height:20px}
.tip-card p{font:400 5px/1.32 var(--sans);color:var(--body)}
.ten-agent{left:370px;top:40px;width:128px;height:195px;background:linear-gradient(180deg,#ffffff 0%,#eef0f2 40%,#d6d9de 100%)}
.cta-line{left:35px;top:183px;display:flex;align-items:center;gap:8px}
.cta-line .script{font-size:26px;color:var(--yellow)}
.cta-rule{width:1px;height:20px;background:var(--yellow)}
.phone-round{width:16px;height:16px;border-radius:50%;background:var(--yellow);display:inline-flex;align-items:center;justify-content:center}
.phone-round svg{width:9px;height:9px;fill:var(--white)}
.cta-number{font:800 20px/1 var(--sans);letter-spacing:.5px}
.priority-line{left:58px;top:212px;display:flex;align-items:baseline;gap:7px}
.priority-line b{font:700 8px/1 var(--sans);letter-spacing:3px}
.priority-line .script{font-size:14px;color:var(--yellow)}

/* Smart way – front */
.smart-agent{left:175px;top:6px;width:215px;height:200px;background:linear-gradient(180deg,#ffffff 0%,#e5eef3 45%,#b7d7e2 75%,#e8e3d6 100%)}
.smart-title{left:16px;top:10px;font:800 19.5px/1.08 var(--sans)}
.smart-script{left:16px;top:82px;font-size:27px;line-height:.95;color:var(--yellow)}
.smart-text{left:16px;top:152px;width:120px;font:500 7.6px/1.33 var(--sans)}
.smart-list{left:381px;top:68px;width:108px}
.smart-list li{list-style:none;display:flex;align-items:center;gap:6px;height:27px;border-bottom:1px solid #e4e4e4;font:500 7.6px/1.2 var(--sans)}
.smart-list li:last-child{border:0}
.smart-list .icon-box{width:16px;height:16px;background:var(--ink)}
.smart-list .icon{stroke:var(--white);width:10px;height:10px}
.band{left:0;bottom:0;width:498px;height:50px}
.band-script{left:186px;top:196px;font-size:18px;transform:rotate(-4deg)}
.band-rule{left:384px;top:199px;width:1px;height:22px;background:var(--ink)}
.band-text{left:395px;top:199px;font:600 8.6px/1.22 var(--sans)}

/* Property report – front */
.report-tile{left:8px;top:12px;width:78px;height:78px;background:var(--yellow);display:flex;align-items:flex-end;justify-content:center;padding-bottom:12px;font:700 11px/1 var(--sans)}
.report-word{left:94px;top:8px;width:140px;font:700 31px/1 var(--cond);white-space:nowrap}
.report-word span{display:block;color:var(--yellow);font-size:55px;line-height:.95;font-weight:500;letter-spacing:-1px}
.report-head{left:252px;top:27px;font:700 10.6px/1 var(--sans);white-space:nowrap}
.report-text{left:252px;top:52px;width:238px;font:500 7.3px/1.33 var(--sans)}
.feature-band{left:0;top:101px;width:498px;height:40px;background:var(--pale);display:flex;padding:6px 8px}
.feature{flex:1;display:flex;gap:6px;align-items:flex-start}
.feature .icon-box{width:17px;height:17px;margin-top:2px}
.feature h4{font:700 7.3px/1.2 var(--sans)}
.feature p{font:400 6.3px/1.3 var(--sans);color:var(--body)}
.worth{left:20px;top:144px;width:270px;text-align:center;font-size:16px;line-height:1.05}
.worth-rule{left:296px;top:147px;width:1px;height:34px;background:#d8d8d8}
.worth-call{left:328px;top:145px;font-size:16px}
.worth-number{left:328px;top:166px;display:flex;align-items:center;gap:4px;font:800 15px/1 var(--sans)}
.worth-number .phone-round{width:12px;height:12px}
.worth-number .phone-round svg{width:7px;height:7px}
.values-bar{left:0;top:190px;width:498px;height:45px;background:var(--yellow);display:flex;align-items:center;padding:0 8px}
.value{display:flex;align-items:center;gap:6px;font:500 9.4px/1.15 var(--sans);width:136px}
.value .icon-box{width:20px;height:20px;background:var(--white)}
.value .icon{width:13px;height:13px}
.value-dot{width:2px;height:6px;background:var(--ink);margin:0 12px 0 0}
.value-brand{margin-left:auto;font:700 11px/1.2 var(--sans);text-align:left}
.value-brand span{display:block;font-weight:500;font-size:8.6px}

/* Ready to sale – front */
.ready-photo{background:linear-gradient(180deg,#dfe5e6 0%,#c8d0c9 15%,#5d7a3f 40%,#4d6b34 60%,#8a8a6d 80%,#b9b096 100%)}
.ready-agent{left:290px;top:8px;width:200px;height:182px;background:linear-gradient(180deg,rgba(255,255,255,.0) 0%,rgba(214,204,186,.55) 30%,rgba(245,245,242,.9) 70%)}
.ready-title{left:15px;top:18px;font:800 24px/1.02 var(--sans);color:var(--white)}
.ready-title span{display:block;color:var(--yellow);font-size:32px;line-height:.95}
.ready-tag{left:15px;top:112px;font:500 9.4px/1 var(--sans);color:var(--white)}
.ready-tag b{font-weight:700}
.ready-rule{left:15px;top:127px;width:160px;height:1px;background:rgba(255,255,255,.8)}
.ready-box{left:15px;top:144px;width:220px;height:43px;background:var(--white);border-radius:6px 6px 0 0;display:flex;padding:6px 10px;gap:18px}
.ready-box .feature h4{font:500 7.8px/1.1 var(--sans)}
.ready-box .feature p{font:500 5.6px/1.3 var(--sans);color:var(--ink);margin-top:2px}
.ready-bar{left:0;top:187px;width:498px;height:48px;background:var(--yellow);display:flex;align-items:center;padding:0 8px;gap:10px}
.ready-bar .script{font-size:22px}
.bar-rule{width:1px;height:26px;background:var(--ink)}
.ready-bar .phone-round{background:var(--ink);width:17px;height:17px}
.ready-bar .phone-round svg{fill:var(--yellow)}
.ready-number{font:800 20.5px/1 var(--sans);letter-spacing:.5px}

/* Ready to sale – back */
.article{top:8px;font:400 5.5px/1.32 var(--sans);color:var(--body)}
.article h3{display:flex;align-items:flex-start;gap:6px;font:700 10px/1.1 var(--sans);color:var(--ink);margin-bottom:7px}
.article h3 .n{flex:none;width:15px;height:17px;background:var(--yellow);font:italic 600 11px/17px var(--sans);text-align:center}
.article .gap{margin-top:12px}
.article-rule{top:10px;width:1px;height:190px;background:var(--yellow)}
.callout{border:1px solid #f2e9a8;background:var(--pale);padding:6px 6px 6px 30px;position:relative;margin-top:18px;height:80px}
.callout .icon-box{position:absolute;left:6px;top:34px;width:17px;height:17px}
.callout h5{font:700 6.6px/1.2 var(--sans);color:var(--ink);margin-bottom:3px}
.quote{border-left:2px solid var(--yellow);padding:4px 0 4px 8px;margin-top:8px;font:600 7.6px/1.3 var(--sans);color:var(--ink)}
.back-bar{left:0;top:206px;width:498px;height:29px;background:var(--yellow);display:flex;align-items:center;gap:12px;padding-left:82px}
.back-bar .script{font-size:17px}
.back-bar b{font:600 6px/1 var(--sans)}
</style>
</head>
<body>

<svg width="0" height="0" style="position:absolute" aria-hidden="true">
  <symbol id="i-home" viewBox="0 0 16 16"><path d="M2 8 8 2.5 14 8M4 7v6.5h8V7M6.5 13.5v-4h3v4"/></symbol>
  <symbol id="i-doc" viewBox="0 0 16 16"><path d="M4 1.5h6l3 3v10H4zM6 7h5M6 9.5h5M6 12h3"/></symbol>
  <symbol id="i-people" viewBox="0 0 16 16"><circle cx="5" cy="5" r="2"/><circle cx="11" cy="5" r="2"/><path d="M1.5 13c0-2.5 1.5-4 3.5-4s3.5 1.5 3.5 4M7.5 13c0-2.5 1.5-4 3.5-4s3.5 1.5 3.5 4"/></symbol>
  <symbol id="i-dollar" viewBox="0 0 16 16"><circle cx="8" cy="8" r="6.5"/><path d="M10 5.5c-.5-.7-1.2-1-2-1-1.2 0-2 .6-2 1.5 0 2 4 1 4 3 0 1-.8 1.6-2 1.6-.9 0-1.6-.4-2-1M8 3.5v9"/></symbol>
  <symbol id="i-chart" viewBox="0 0 16 16"><path d="M2 14h12M4 13V9M7 13V6M10 13V8M13 13V3"/></symbol>
  <symbol id="i-heart" viewBox="0 0 16 16"><path d="M8 14S1.5 10 1.5 5.5A3.2 3.2 0 0 1 8 4a3.2 3.2 0 0 1 6.5 1.5C14.5 10 8 14 8 14z"/></symbol>
  <symbol id="i-tool" viewBox="0 0 16 16"><path d="M10 2a3.5 3.5 0 0 0-3 5L2 12l2 2 5-5a3.5 3.5 0 0 0 5-3l-2 1-2-2z"/></symbol>
  <symbol id="i-check" viewBox="0 0 16 16"><rect x="2" y="2" width="12" height="12" rx="1"/><path d="m5 8 2 2 4-4"/></symbol>
  <symbol id="i-key" viewBox="0 0 16 16"><circle cx="5" cy="8" r="3"/><path d="M8 8h6.5M12 8v2.5M14 8v2"/></symbol>
  <symbol id="i-phone" viewBox="0 0 16 16"><path d="M4 1.5 6.5 4 5 6a9 9 0 0 0 5 5l2-1.5 2.5 2.5-2 2C7 14 2 9 2 3.5z"/></symbol>
</svg>

<!-- ROW 1 : STEPS OF A SALE -->
<section class="card col-l row-1">
  <div class="photo steps-photo" role="img" aria-label="Photo of a woman walking along a turquoise beach below a green headland"></div>
  <h1 class="abs steps-title">STEPS<br><span>OF A SALE</span></h1>
  <p class="abs steps-sub">A clear process. Proven results. From listing to settlement, I'm with you every step of the way.</p>
  <div class="brand-tile">Fen Calder</div>
  <div class="abs site-url">www.fencalder.com</div>
</section>

<section class="card col-r row-1">
  <div class="abs step-col" style="left:7px">
    <div class="step-head"><span class="step-num">1</span><span class="step-title">Preparation<br>&amp; Appraisal</span></div>
    <div class="step-item"><span class="icon-box"><svg class="icon"><use href="#i-people"/></svg></span><div><h4>Agent Selection</h4><p>Choose a local agent and set a realistic selling price based on market research.</p></div></div>
    <div class="step-item"><span class="icon-box"><svg class="icon"><use href="#i-home"/></svg></span><div><h4>Home Styling</h4><p>Clean, declutter, and repair flaws to make the property photogenic. You can read seven important tips for a successful sale from Fen Calder for guidance on staging your home.</p></div></div>
    <div class="step-item"><span class="icon-box"><svg class="icon"><use href="#i-doc"/></svg></span><div><h4>Contract Preparation</h4><p>Work with a solicitor or conveyancer to prepare the contract of sale and vendor statement.</p></div></div>
    <div class="tip"><b>FEN CALDER TIP:</b>Good preparation can make a big difference to how buyers see your property.</div>
  </div>
  <div class="abs step-col" style="left:106px">
    <div class="step-head"><span class="step-num">2</span><span class="step-title">Choosing a<br>Method of Sale</span></div>
    <div class="step-item"><span class="icon-box"><svg class="icon"><use href="#i-tool"/></svg></span><div><h4>Auction</h4><p>Set a date, market without a price to build urgency, and encourage competitive bidding.</p></div></div>
    <div class="step-item"><span class="icon-box"><svg class="icon"><use href="#i-people"/></svg></span><div><h4>Private Treaty</h4><p>List an asking price and negotiate individual offers with buyers.</p></div></div>
    <div class="step-item"><span class="icon-box"><svg class="icon"><use href="#i-doc"/></svg></span><div><h4>Expressions of Interest / Tender</h4><p>Invite confidential offers by a set date for unique properties.</p></div></div>
    <div class="tip"><b>FEN CALDER TIP:</b>The right method of sale depends on your property, the local market and your goals. Your agent can recommend the strategy best suited to a strong result.</div>
  </div>
  <div class="abs step-col" style="left:205px">
    <div class="step-head"><span class="step-num">3</span><span class="step-title">Marketing<br>&amp; Campaign</span></div>
    <div class="step-item"><span class="icon-box"><svg class="icon"><use href="#i-chart"/></svg></span><div><h4>Launch your Campaign</h4><p>Present your property to the market with professional photography, online advertising, signage and targeted promotion.</p></div></div>
    <div class="step-item"><span class="icon-box"><svg class="icon"><use href="#i-home"/></svg></span><div><h4>Inspections</h4><p>Hold open homes and private viewings to give prospective buyers the opportunity to experience your property.</p></div></div>
    <div class="step-item"><span class="icon-box"><svg class="icon"><use href="#i-doc"/></svg></span><div><h4>Vendor Reports</h4><p>Receive regular updates from your agent covering buyer feedback, inspection numbers, enquiry levels and overall market interest.</p></div></div>
    <div class="tip"><b>FEN CALDER TIP:</b>A strong marketing campaign creates exposure, builds buyer interest and helps generate competition for your property.</div>
  </div>
  <div class="abs step-col" style="left:304px;width:108px">
    <div class="step-head"><span class="step-num">4</span><span class="step-title">Contract Exchange<br>&amp; Settlement</span></div>
    <div class="step-item"><span class="icon-box"><svg class="icon"><use href="#i-doc"/></svg></span><div><h4>Exchange</h4><p>Both buyer and seller sign separate copies of the contract, and they are swapped.</p></div></div>
    <div class="step-item"><span class="icon-box"><svg class="icon"><use href="#i-dollar"/></svg></span><div><h4>Deposit</h4><p>The buyer pays a deposit (usually 10%), which is held in a trust account.</p></div></div>
    <div class="step-item"><span class="icon-box"><svg class="icon"><use href="#i-check"/></svg></span><div><h4>Cooling-off</h4><p>Private treaty sales usually include a 5-day cooling-off period for buyers (none at auction).</p></div></div>
    <div class="step-item"><span class="icon-box"><svg class="icon"><use href="#i-key"/></svg></span><div><h4>Settlement</h4><p>The final transaction is completed, typically 42 days (six weeks) after exchange, and keys are handed over.</p></div></div>
    <div class="tip"><b>FEN CALDER TIP:</b>Your agent, solicitor or conveyancer will guide you through the final steps from exchange through to settlement and key handover.</div>
  </div>
  <aside class="abs agent-panel">
    <div class="agent-photo abs" role="img" aria-label="Portrait photo of agent Jack in a white shirt"></div>
    <p class="abs agent-note">If you are thinking of selling, planning to sell or would simply like to chat about your options.</p>
    <p class="abs agent-call">Reach out and<span>call me today.</span></p>
    <div class="abs agent-name script">Jack</div>
    <div class="abs phone-bar"><span class="phone-dot"><svg viewBox="0 0 16 16"><use href="#i-phone"/></svg></span>0400 123 456</div>
  </aside>
  <div class="brand-tile">Fen Calder</div>
</section>

<!-- ROW 2 : 10 THINGS -->
<section class="card col-l row-2">
  <div class="photo sunset-photo" role="img" aria-label="Photo of a camel train walking along a beach at sunset, reflected in wet sand"></div>
  <h1 class="abs ten-title">10 THINGS<span>TO GET YOUR</span><span>PROPERTY</span></h1>
  <div class="abs ten-script script">Ready to Sell</div>
  <div class="abs ten-rule"></div>
  <p class="abs ten-note">A well-prepared home makes a lasting first impression and helps achieve the best result.</p>
  <div class="brand-tile">Fen Calder</div>
  <div class="abs site-url">www.fencalder.com</div>
</section>

<section class="card col-r row-2">
  <div class="abs ten-agent" role="img" aria-label="Portrait photo of agent Jack smiling in a white shirt"></div>
  <div class="abs tip-grid">
    <div class="tip-card"><span class="n">1</span><svg class="icon"><use href="#i-home"/></svg><h4>Clean &amp;<br>Declutter</h4><p>Remove personal items and clutter. A clean, tidy home feels bigger, brighter and more inviting.</p></div>
    <div class="tip-card"><span class="n">2</span><svg class="icon"><use href="#i-tool"/></svg><h4>Finish Projects<br>&amp; Repairs</h4><p>Fix minor issues, leaky taps, loose handles and any repairs buyers will notice.</p></div>
    <div class="tip-card"><span class="n">3</span><svg class="icon"><use href="#i-doc"/></svg><h4>Do a Thorough<br>Inspection</h4><p>Check the big and small things - inside and out so there are no surprises later.</p></div>
    <div class="tip-card"><span class="n">4</span><svg class="icon"><use href="#i-tool"/></svg><h4>Paint</h4><p>A fresh coat of neutral paint can transform your home and make it feel well maintained.</p></div>
    <div class="tip-card"><span class="n">5</span><svg class="icon"><use href="#i-check"/></svg><h4>Freshen up<br>Fixtures &amp;<br>Hardware</h4><p>Update old light fittings, tapware and cabinet handles for an instant lift.</p></div>
    <div class="tip-card"><span class="n">6</span><svg class="icon"><use href="#i-home"/></svg><h4>Clean or Replace<br>Flooring</h4><p>Clean carpets, tiles and floors or replace if needed. Great floors make a big difference.</p></div>
    <div class="tip-card"><span class="n">7</span><svg class="icon"><use href="#i-key"/></svg><h4>Create a<br>Welcoming<br>Entrance</h4><p>Tidy up the front yard, clean the entry and add plants for great street appeal.</p></div>
    <div class="tip-card"><span class="n">8</span><svg class="icon"><use href="#i-home"/></svg><h4>Stage Your<br>Home</h4><p>Arrange furniture to showcase space and lifestyle. Less is more when selling.</p></div>
    <div class="tip-card"><span class="n">9</span><svg class="icon"><use href="#i-heart"/></svg><h4>Eliminate<br>Odours</h4><p>Remove pet smells, smoke, cooking and musty odours for a fresh, neutral home.</p></div>
    <div class="tip-card"><span class="n">10</span><svg class="icon"><use href="#i-dollar"/></svg><h4>Get Your<br>Real Price</h4><p>Work with an agent to set the right price and attract the right buyers.</p></div>
  </div>
  <div class="abs cta-line"><span class="script">Call Jack</span><span class="cta-rule"></span><span class="phone-round"><svg viewBox="0 0 16 16"><use href="#i-phone"/></svg></span><span class="cta-number">0400 123 456</span></div>
  <div class="abs priority-line"><b>YOUR PROPERTY</b><span class="script">Our Priority</span></div>
  <div class="brand-tile">Fen Calder</div>
</section>

<!-- ROW 3 : SMART WAY / PROPERTY REPORT -->
<section class="card col-l row-3">
  <div class="abs smart-agent" role="img" aria-label="Photo of agent Jack in a white shirt standing by a beach"></div>
  <h1 class="abs smart-title">The smart<br>way to sell<br>your property</h1>
  <div class="abs smart-script script">Start with<br>knowledge.</div>
  <p class="abs smart-text">Inspect your property before you sell and give buyers confidence from day one.</p>
  <ul class="abs smart-list">
    <li><span class="icon-box"><svg class="icon"><use href="#i-home"/></svg></span>Know what needs<br>attention</li>
    <li><span class="icon-box"><svg class="icon"><use href="#i-doc"/></svg></span>Fix issues and<br>improve value</li>
    <li><span class="icon-box"><svg class="icon"><use href="#i-people"/></svg></span>Build buyer<br>confidence</li>
    <li><span class="icon-box"><svg class="icon"><use href="#i-dollar"/></svg></span>Market with<br>confidence</li>
  </ul>
  <svg class="abs band" viewBox="0 0 498 50" preserveAspectRatio="none" aria-hidden="true"><polygon points="0,20 498,0 498,50 0,50" fill="#ffe600"/></svg>
  <div class="abs band-script script">Your property. Our priority.</div>
  <div class="abs band-rule"></div>
  <div class="abs band-text">Let's achieve your<br>next move together.</div>
  <div class="brand-tile">Fen Calder</div>
</section>

<section class="card col-r row-3">
  <div class="abs report-tile">Fen Calder</div>
  <h1 class="abs report-word">PROPERTY<span>REPORT</span></h1>
  <h2 class="abs report-head">What's in the Fen Calder property report?</h2>
  <p class="abs report-text">The Fen Calder Property Report gives you an in-depth understanding of your property and the market with comprehensive data including property value estimates, comparable sales and historical suburb performance.</p>
  <div class="abs feature-band">
    <div class="feature"><span class="icon-box"><svg class="icon"><use href="#i-home"/></svg></span><div><h4>IN-DEPTH</h4><p>Comprehensive insights into<br>your property.</p></div></div>
    <div class="feature"><span class="icon-box"><svg class="icon"><use href="#i-chart"/></svg></span><div><h4>MARKET DATA</h4><p>Up-to-date local market trends<br>and performance.</p></div></div>
    <div class="feature"><span class="icon-box"><svg class="icon"><use href="#i-doc"/></svg></span><div><h4>CLEAR REPORT</h4><p>Easy to understand,<br>well-presented report.</p></div></div>
  </div>
  <div class="abs worth script">Want to know what your property<br>could be worth?</div>
  <div class="abs worth-rule"></div>
  <div class="abs worth-call script">Call Jack</div>
  <div class="abs worth-number"><span class="phone-round"><svg viewBox="0 0 16 16"><use href="#i-phone"/></svg></span>0400 123 456</div>
  <div class="abs values-bar">
    <div class="value"><span class="icon-box"><svg class="icon"><use href="#i-home"/></svg></span>Local<br>Knowledge.</div><span class="value-dot"></span>
    <div class="value"><span class="icon-box"><svg class="icon"><use href="#i-people"/></svg></span>Exceptional<br>Service.</div><span class="value-dot"></span>
    <div class="value" style="width:110px"><span class="icon-box"><svg class="icon"><use href="#i-heart"/></svg></span>Genuine<br>Care.</div>
    <div class="value-brand">Fen Calder<span>Harbour Bay</span></div>
  </div>
</section>

<!-- ROW 4 : READY TO SELL / INSPECTION ARTICLE -->
<section class="card col-l row-4">
  <div class="photo ready-photo" role="img" aria-label="Photo of coastal houses above green scrub and a sandy path"></div>
  <div class="abs ready-agent" role="img" aria-label="Portrait photo of agent Jack smiling in a white shirt"></div>
  <h1 class="abs ready-title">IS YOUR<span>PROPERTY</span>READY TO SALE?</h1>
  <p class="abs ready-tag">Local knowledge. <b>Exceptional service.</b></p>
  <div class="abs ready-rule"></div>
  <div class="abs ready-box">
    <div class="feature"><span class="icon-box"><svg class="icon"><use href="#i-home"/></svg></span><div><h4>LOCAL<br>KNOWLEDGE</h4><p>We know the area.</p></div></div>
    <div class="feature"><span class="icon-box"><svg class="icon"><use href="#i-people"/></svg></span><div><h4>EXCEPTIONAL<br>SERVICE</h4><p>We put you first.</p></div></div>
  </div>
  <div class="abs ready-bar">
    <span class="script">Call Jack</span><span class="bar-rule"></span>
    <span class="phone-round"><svg viewBox="0 0 16 16"><use href="#i-phone"/></svg></span><span class="ready-number">0400 123 456</span><span class="bar-rule"></span>
    <span class="script" style="font-size:17px">Your property. Our priority.</span>
  </div>
  <div class="brand-tile">Fen Calder</div>
</section>

<section class="card col-r row-4">
  <div class="abs article" style="left:8px;width:142px">
    <h3><span class="n">1</span>Getting things fixed:</h3>
    <p>One of the biggest advantages is that you can improve the condition of the property if you know there are things that can be fixed. This makes it a much better product to market.</p>
    <h3 class="gap"><span class="n">2</span>Getting this reflected in the report:</h3>
    <p>Fixing issues means fixing them to the satisfaction of the building inspector. When this is done properly, the inspector can update his report to reflect the improved condition of the property, giving the owner more confidence in marketing their property and giving buyers more confidence in the property itself.</p>
  </div>
  <div class="abs article-rule" style="left:156px"></div>
  <div class="abs article" style="left:164px;width:154px">
    <h3><span class="n">3</span>Making the report available to buyers:</h3>
    <p>Another big advantage of inspecting your property before marketing it is that the inspection report can then be available to buyers at the beginning of the campaign. This means buyers can carry out their checks faster and, usually, at a lower cost.</p>
    <p style="margin-top:5px;color:var(--ink);font-weight:600">However it's very important that this process is done professionally.</p>
    <div class="callout"><span class="icon-box"><svg class="icon"><use href="#i-home"/></svg></span><h5>What if the property has serious issues?</h5><p>Some issues can't be fixed easily - like rising damp or wall cracks - but it's much better to know what you're dealing with and have a strategy for managing those issues with buyers. For example, wall cracks could be checked by a structural engineer.</p></div>
  </div>
  <div class="abs article-rule" style="left:328px"></div>
  <div class="abs article" style="left:340px;width:150px">
    <p>For the example above, the owner could've addressed the issue before marketing. He could've had the pest infestation eliminated by a pest controller and had the timber damage assessed and repaired by a qualified tradesperson. Then the inspector could have attended the property to assess the property condition again.</p>
    <div class="quote">Always remember - if your listing is in good condition, why wouldn't you want buyers to know that?</div>
    <div class="callout" style="margin-top:12px;height:72px"><span class="icon-box" style="top:28px"><svg class="icon"><use href="#i-people"/></svg></span><p style="margin-top:14px">If buyers can access better information about the property and get professional follow up support for a low fee, it's likely to be one of the best ways to market a property.</p></div>
  </div>
  <div class="abs back-bar"><span class="script">Your property. Our priority.</span><span class="bar-rule" style="height:14px"></span><b>Let's achieve your next move together.</b></div>
</section>

</body>
</html>
```